Quorvex clinic business card - double sided for young clinic

I require business cards for my aesthetic clinic specialising in the below treatments. I would like the cards to be modern as my clinic base are young 22-35 years old. I require my logo on it and would like the edges to be rounded.

I have an aesthetic clinic specialising in :
Quorvex
Lip Enhancement
Chemical Peels
Facial Fillers
Non Surgical Face Lift

I would the cards to have the following information on them:
My logo - (in grey/silver)
address
Phone number
services

Colours :
White/grey/silver and red

a nice image on there, perhaps a set of lips as this is a main service i deliver

Company Name: PDA Address: 52 Farrowmere Road, 4 Brackwell High Street, KT9 4WQ Phone: 0208 794 2160 Website: www.penningtondoweaesthetics.co.uk

Target Market(s)

clinics 22-45 years old mainly female

Industry/Entity Type

Business

Contact Information for Business Card

as above

Requirements
Must have
• logo
• Address
• Email
• Phone number
• Services i offer
Nice to have
• images

```html
<!DOCTYPE html>
<html lang="en">
<head>
<meta charset="UTF-8">
<title>PDA Business Card – Front and Back</title>
<link href="https://fonts.googleapis.com/css2?family=Libre+Baskerville:wght@400;700&family=Open+Sans:wght@700&display=swap" rel="stylesheet">
<style>
  :root {
    --page-bg: #e6e7e6;
    --card-dark: #4a4a4e;
    --card-white: #ffffff;
    --brand-red: #e5232b;
    --brand-grey: #56565a;
    --text-light: #e9e9ea;
    --rule-light: #bdbdc0;
  }
  * { margin: 0; padding: 0; box-sizing: border-box; }
  html, body { width: 1200px; height: 1200px; overflow: hidden; }
  body {
    background: var(--page-bg);
    font-family: "Libre Baskerville", Georgia, serif;
    position: relative;
  }
  .card {
    position: absolute;
    left: 250px;
    width: 700px;
    height: 400px;
    overflow: hidden;
    box-shadow: 0 4px 10px rgba(0,0,0,0.18);
  }
  .card--front { top: 150px; background: var(--card-dark); }
  .card--back  { top: 650px; background: var(--card-white); }

  .card__panel { position: absolute; inset: 0; }

  /* logo lockup */
  .brand { position: absolute; text-align: center; }
  .brand__mark {
    display: flex; align-items: center; justify-content: center; gap: 10px;
    font-weight: 400;
  }
  .brand__dot { border-radius: 50%; display: inline-block; }
  .brand__name-top, .brand__name-bottom { display: block; font-weight: 400; letter-spacing: 0.12em; line-height: 1; }

  .card--front .brand { left: 22px; top: 135px; width: 250px; color: var(--brand-red); }
  .card--front .brand__mark { font-size: 34px; margin-bottom: 22px; }
  .card--front .brand__dot { width: 22px; height: 22px; background: var(--brand-red); }
  .card--front .brand__name-top { font-size: 15px; }
  .card--front .brand__name-bottom { font-size: 22px; margin-top: 3px; }

  .card--back .brand { left: 0; right: 0; top: 100px; color: var(--brand-grey); }
  .card--back .brand__mark { font-size: 64px; margin-bottom: 40px; }
  .card--back .brand__dot { width: 40px; height: 40px; background: var(--brand-grey); }
  .card--back .brand__name-top { font-size: 28px; }
  .card--back .brand__name-bottom { font-size: 40px; margin-top: 6px; }

  /* front: contact side */
  .title {
    position: absolute; left: 350px; top: 36px;
    color: var(--text-light); font-size: 46px; font-weight: 400; line-height: 1;
  }
  .title__role { font-size: 19px; letter-spacing: 0.04em; margin-left: 10px; }

  .contact { position: absolute; left: 355px; top: 148px; width: 310px; }
  .contact__divider {
    position: absolute; left: 42px; top: 4px; width: 1px; height: 108px; background: var(--rule-light);
  }
  .contact__row { display: flex; align-items: center; height: 38px; }
  .contact__icon { width: 22px; height: 22px; margin-left: 4px; flex: none; }
  .contact__text {
    margin-left: 40px; flex: 1; color: var(--text-light); font-size: 15px;
    border-bottom: 1px solid var(--rule-light); padding-bottom: 4px; line-height: 1.4;
  }

  .services { position: absolute; left: 282px; top: 300px; color: var(--text-light); }
  .services__heading {
    font-family: "Open Sans", Arial, sans-serif; font-weight: 700; font-size: 15px;
    margin-left: 14px; margin-bottom: 10px;
  }
  .services__list { list-style: none; display: flex; flex-wrap: wrap; width: 410px; row-gap: 6px; column-gap: 8px; }
  .services__item { display: flex; align-items: center; font-size: 15px; white-space: nowrap; }
  .services__tick { width: 12px; height: 12px; margin-right: 5px; flex: none; }
</style>
</head>
<body>

<section class="card card--front" aria-label="Business card front">
  <svg class="card__panel" viewBox="0 0 700 400" aria-hidden="true">
    <path d="M0 0 H170 C260 20 305 110 305 190 C305 280 260 350 185 400 H0 Z" fill="#ffffff"/>
  </svg>

  <div class="brand">
    <div class="brand__mark"><span class="brand__dot"></span>PDA</div>
    <span class="brand__name-top">PENNINGTON DOWE</span>
    <span class="brand__name-bottom">AESTHETICS</span>
  </div>

  <h1 class="title">PDA<span class="title__role">(PHYSICIAN)</span></h1>

  <div class="contact">
    <span class="contact__divider"></span>
    <div class="contact__row">
      <svg class="contact__icon" viewBox="0 0 24 24" fill="none" stroke="#e9e9ea" stroke-width="2"><path d="M12 20s-6-6.5-6-11a6 6 0 0 1 12 0c0 4.5-6 11-6 11z"/><circle cx="12" cy="9" r="2"/><path d="M6 23h12"/></svg>
      <span class="contact__text">52 Farrowmere Road, KT9 4WQ</span>
    </div>
    <div class="contact__row">
      <svg class="contact__icon" viewBox="0 0 24 24" fill="#e9e9ea"><path d="M6.6 3.5l3 3.2-1.8 2c.9 2.6 2.8 4.6 5.4 5.6l2-1.7 3.3 3-1.7 2.6C10.4 18.5 5 12.9 4.2 6z"/></svg>
      <span class="contact__text">0208 794 2160</span>
    </div>
    <div class="contact__row">
      <svg class="contact__icon" viewBox="0 0 24 24" fill="none" stroke="#e9e9ea" stroke-width="2"><circle cx="12" cy="12" r="10"/><rect x="6.5" y="8" width="11" height="8"/><path d="M6.5 8l5.5 4.5L17.5 8"/></svg>
      <span class="contact__text">info@pda.com</span>
    </div>
  </div>

  <div class="services">
    <h2 class="services__heading">SERVICES :-</h2>
    <ul class="services__list">
      <li class="services__item"><svg class="services__tick" viewBox="0 0 12 12"><circle cx="6" cy="6" r="6" fill="#e9e9ea"/><path d="M3.3 6.2l1.8 1.8 3.6-3.7" stroke="#4a4a4e" stroke-width="1.6" fill="none"/></svg>Quorvex</li>
      <li class="services__item"><svg class="services__tick" viewBox="0 0 12 12"><circle cx="6" cy="6" r="6" fill="#e9e9ea"/><path d="M3.3 6.2l1.8 1.8 3.6-3.7" stroke="#4a4a4e" stroke-width="1.6" fill="none"/></svg>Lip Enhancement</li>
      <li class="services__item"><svg class="services__tick" viewBox="0 0 12 12"><circle cx="6" cy="6" r="6" fill="#e9e9ea"/><path d="M3.3 6.2l1.8 1.8 3.6-3.7" stroke="#4a4a4e" stroke-width="1.6" fill="none"/></svg>Chemical Peels</li>
      <li class="services__item"><svg class="services__tick" viewBox="0 0 12 12"><circle cx="6" cy="6" r="6" fill="#e9e9ea"/><path d="M3.3 6.2l1.8 1.8 3.6-3.7" stroke="#4a4a4e" stroke-width="1.6" fill="none"/></svg>Facial Fillers</li>
      <li class="services__item"><svg class="services__tick" viewBox="0 0 12 12"><circle cx="6" cy="6" r="6" fill="#e9e9ea"/><path d="M3.3 6.2l1.8 1.8 3.6-3.7" stroke="#4a4a4e" stroke-width="1.6" fill="none"/></svg>Non Surgical Face Lift</li>
    </ul>
  </div>
</section>

<section class="card card--back" aria-label="Business card back">
  <div class="brand">
    <div class="brand__mark"><span class="brand__dot"></span>PDA</div>
    <span class="brand__name-top">PENNINGTON DOWE</span>
    <span class="brand__name-bottom">AESTHETICS</span>
  </div>
</section>

</body>
</html>
```